GUARANTEED! - Creation of Linqora Promotional Images (requires Photoshops to modify cars)

Hi all,

We will require 5 different images to be created although once the first one is completed, the look and theme can literally be copied across to the others. These promotional images are to represent the service our website offers as well as the benefit’s the user can receive. (please ask for the website via private message if required) Our website is literally a comparison website related to vehicle modifications - so we make it quick and easy for users to find the best deal with local Window Tinters, ECU Remappers, Alloy Wheel Refurbs & More.

Aim of the image - This is purely to be posted on linqora to push viewers to our website / linqora page (there will be links in the description when it’s posted on linqora) so the image needs to tell the user what we do and urge them to visit the website.

Target market - our target market is mainly the car enthusiast (ages between 17 - 25) although we’re looking to keep this promotional image simple, professional and with the use of light neutral colours.

Image to be created - (our idea, please feel free to change) - see attachment of rough sketch created titled : ‘Rough Sketch Promotional Image

Main title across the top will read ‘FIND THE BEST DEAL WITH :’ - The words best deal should stand out more and be of a larger font / potentially different colour, maybe orange to keep in theme with the website. Then as shown in the sketch, we will have car number 1 which has been photoshopped as stated further down . Then we will have arrows pointing onto the car which will state the different modifications that has been completed on the car e.g - arrow will point to the rear window and will state the words :

WINDOW TINTERS
IN YOUR AREA

(regarding the text stated above, we feel it would be best if they were all placed the same distance away from the car to keep the professional look) - we also feel the service mentioned such as ‘WINDOW TINTERS’ should be a larger font than the ‘IN YOUR AREA’

Each car will have 4 arrows pointing on different parts of the car with text added as stated above (hopefully the rough sketch will make all these requirements that little bit clearer)

Then underneath the car image with the 4 arrows and text, we will have a Call to action button (which should keep the same kind of theme as that on the website homepage, (green blackground of block with white text) - The text in this button will read ‘CLICK BELOW!’ - we also had the idea of adding an arrow under the Call to action button to point the users to the description below the image. (Needs to be clear space around the CTA so it stands out - apart from potentially this arrow)

Then finally we’d like to have our logo (quite small) to the bottom left of the image with the words ‘PLEASE SHARE!’ to the bottom right of the image.

As you can see, the requirements we’re after are quite simple so the time will be mostly in the photoshopping of the 5 cars.

Please refer to the rough sketch but if you have any questions, please contact us here.

PHOTOSHOPS REQUIRED

The changes made to each car will be partly left up to you - however it’s vitally important that it stands out yet doesn’t look ‘silly’ and needs to look realistic - looking realistic is important.

Photoshop requirements

Car 1 - Green Valtessa

- Possibly change colour - please feel free to try other colours (need to look realistic)
- Change the colour of the rear window to a limo style black.
- Change the colour of the roof (can only see a slight bit of it) to black
- Change the colour of the wheels (the colour used here will depend on the change colour of the actual car, some options we like include yellow, green, orange and red

Car 2 - White Korvane LX5

- Change the colour of the rear window and rear side window to a limo style black
- Change the colour of the roof to black (not decided whether it should be black/matt black so test)
- Change the colour of the wheels to a red/ orange

Car 3 - Blue Brivo

- Possibly change colour - please feel free to try other colours - maybe a red but needs to look realistic
- Change the colour of the rear window visible to a limo style black
- Change the colour of the roof to black
- Change the colour of the wheels to black

Car 4 - Yellow Korvane LX5

- Please try changing the colour of this to a metallic grey/dark silver / gloss dark blue.
- Change the colour of the wheels to a yellow

Car 5 - Black Korvane LX5 (first of all we need to remove the background of this image)

Please state if this is too difficult to photoshop and we’ll go from there.

- Colour change to red please - ensure looks realistic
- Change the colour of the wheels to a black

If any of the changes we’ve requested don’t look realistic when you’ve created them - please let us know and feel free to try other colours … remember, needs to look professional and realistic.

Background - up to you although we feel something quite neutral would work well - please however try out whatever you think would look good.

************* IMPORTANT - PLEASE READ *******************

To save you time and to avoid wasted effort, we'd like you to create the promotional image using image 1 ONLY first of all - once we're satisfied with that 100%, we would then ask you to complete the other 4 images (which shouldn't take long once the first image is complete)

*************************************************************************

Just to add - we have purchased the rights for these images but if you feel you've some car images that would suit our requirements better than these, please send them across to us for our opinion.

We may add to this brief so keep an eye out - we will also offer additional work to the winning designer - if you have any questions at all, please ask away.

Thanks,

Derek,
Updates

Still not there with the design all - keep them coming.Thanks Added Saturday, October 1, 2016

Project Deadline Extended Reason: Not happy with the designs receivec and only received a few different designers whereas the project I purchased stated I would receive alot more..Not impressed so far.Regards.Derek Added Monday, October 3, 2016

Target Market(s)

Car enthusiast / youthful - but needs to have the professional clear look - most important.

Industry/Entity Type

Promotional

Font styles to use
Serif
Sans Serif

Requirements
Must have
• - Title of 'FIND THE BEST DEAL WITH : '
• - Car image for each
• - 4 Arrows coming off car for each image with the text stated
• - Call to action button - that stands out
• - Logo and words 'Please share!' / 'Please share me!'
Nice to have
• Potential other car images (would need commercial right so would have to be free for commercial use or a suitable price to pay for the rights) - this is only if you feel you have an image that would be better than those we currently have.
Should not have
• Needs to be kept clear - points to stand out are the opening title of 'FIND THE BEST DEAL WITH :', Car and the service such as 'WINDOW TINTERS'

```html
<!DOCTYPE html>
<html lang="en">
<head>
<meta charset="utf-8">
<title>Find the Best Deal – Promotional Image</title>
<link rel="stylesheet" href="https://fonts.googleapis.com/css2?family=Roboto:ital,wght@0,400;1,900&family=Arimo:wght@400&display=swap">
<style>
  :root {
    --stage: #111111;
    --paper: #ffffff;
    --ink: #2b2b2b;
    --muted: #6a6a6a;
    --orange: #f26a10;
    --green: #14a01c;
    --line: #a8a8a8;
    --box-edge: #cfcfcf;
  }
  * { margin: 0; padding: 0; box-sizing: border-box; }
  html, body { width: 1200px; height: 1200px; overflow: hidden; background: var(--stage); }
  .promo {
    position: absolute; left: 100px; top: 100px;
    width: 1000px; height: 1000px;
    background: var(--paper);
    font-family: "Roboto", Arial, sans-serif;
  }
  .promo__topbar { position: absolute; left: 0; top: 0; width: 100%; height: 10px; background: var(--orange); }
  .headline {
    position: absolute; left: 0; top: 38px; width: 100%;
    text-align: center; font-style: italic; font-weight: 900;
    color: var(--ink); font-size: 44px; letter-spacing: 1px; white-space: nowrap;
  }
  .headline__accent { color: var(--orange); font-size: 72px; letter-spacing: 2px; margin: 0 8px; }
  .service {
    position: absolute; text-align: center;
    background: linear-gradient(#ffffff 45%, #e6e6e6);
    border: 2px solid var(--box-edge);
    box-shadow: 0 3px 6px rgba(0,0,0,.18);
    padding-top: 12px;
  }
  .service__name { display: block; font-style: italic; font-weight: 900; font-size: 22px; color: var(--ink); letter-spacing: 1px; }
  .service__area { display: block; font-family: "Arimo", Arial, sans-serif; font-size: 22px; color: var(--muted); line-height: 1.1; }
  .service--roof { left: 66px; top: 178px; width: 342px; height: 86px; }
  .service--tint { left: 588px; top: 178px; width: 342px; height: 86px; }
  .service--wheel { left: 66px; top: 652px; width: 366px; height: 88px; }
  .service--ecu { left: 570px; top: 652px; width: 360px; height: 88px; }
  .car-photo {
    position: absolute; left: 192px; top: 350px; width: 630px; height: 240px;
    background: radial-gradient(ellipse at 50% 55%, #f4f5f7 0%, #dfe2e6 45%, #ffffff 75%);
    border-radius: 40px;
  }
  .connectors { position: absolute; left: 0; top: 0; }
  .cta {
    position: absolute; left: 302px; top: 802px; width: 394px; height: 80px;
    background: var(--green); color: #fff;
    display: flex; align-items: center; justify-content: center;
    font-style: italic; font-weight: 900; font-size: 30px; letter-spacing: 1px;
  }
  .footer-brand {
    position: absolute; left: 32px; top: 938px; padding: 0 8px 4px;
    border-bottom: 2px solid var(--ink);
    font-style: italic; font-weight: 900; font-size: 26px; color: var(--ink); letter-spacing: 1px;
  }
  .share {
    position: absolute; right: 30px; top: 936px;
    display: flex; align-items: center; gap: 14px;
    font-style: italic; font-weight: 900; font-size: 28px; color: var(--ink); letter-spacing: 1px;
  }
</style>
</head>
<body>
  <main class="promo">
    <div class="promo__topbar"></div>
    <h1 class="headline">FIND THE <span class="headline__accent">BEST DEAL</span> WITH:</h1>

    <div class="car-photo" role="img" aria-label="White Korvane LX5 sports car in side view with tinted rear windows, black roof and orange wheels"></div>

    <svg class="connectors" width="1000" height="1000" viewBox="0 0 1000 1000" aria-hidden="true">
      <g fill="none" stroke="var(--line)" stroke-width="2">
        <polyline points="492,264 492,360"/>
        <polyline points="930,264 930,400 540,400"/>
        <polyline points="930,652 930,450 800,450"/>
        <polyline points="66,652 66,530 250,530"/>
      </g>
      <g fill="var(--orange)">
        <polygon points="484,358 500,358 492,376"/>
        <polygon points="542,392 542,408 524,400"/>
        <polygon points="802,442 802,458 784,450"/>
        <polygon points="248,522 248,538 266,530"/>
      </g>
    </svg>

    <div class="service service--roof"><span class="service__name">ROOF VINYL WRAPPERS</span><span class="service__area">in your Area</span></div>
    <div class="service service--tint"><span class="service__name">WINDOW TINTERS</span><span class="service__area">in your Area</span></div>
    <div class="service service--wheel"><span class="service__name">ALLOY WHEEL REFURBISH</span><span class="service__area">in your Area</span></div>
    <div class="service service--ecu"><span class="service__name">ECU REMAP</span><span class="service__area">in your Area</span></div>

    <div class="cta">SEARCH FOR FREE !</div>
    <svg class="connectors" width="1000" height="1000" viewBox="0 0 1000 1000" aria-hidden="true">
      <polygon points="454,890 544,890 499,982" fill="var(--green)"/>
    </svg>

    <div class="footer-brand">TUNELOCAL</div>
    <div class="share">
      <svg width="44" height="44" viewBox="0 0 44 44" aria-hidden="true">
        <g fill="var(--orange)" stroke="var(--orange)" stroke-width="4">
          <line x1="12" y1="22" x2="33" y2="9"/>
          <line x1="12" y1="22" x2="33" y2="35"/>
          <circle cx="10" cy="22" r="6"/>
          <circle cx="34" cy="8" r="6"/>
          <circle cx="34" cy="36" r="6"/>
        </g>
      </svg>
      <span>Please Share Me</span>
    </div>
  </main>
</body>
</html>
```